Email Signature

Our company is having its 10th anniversary in 2021. We would like a new email signature to celebrate the occasion. Attached is our business card design.
Please refer to our website for actual contact details.
www.corvanhold.com.au

Industry/Entity Type

Real Estate

Requirements
Must have
• Our logo
Email
Contact Numbers
Address
Website address

Celebrating 10 years in 2021
Nice to have
• Something that blends the designs of our website and business card

```html
<!DOCTYPE html>
<html lang="en">
<head>
<meta charset="utf-8">
<title>Corvan Hold – Email Signature</title>
<link rel="stylesheet" href="https://fonts.googleapis.com/css2?family=Noto+Serif:ital,wght@0,400;0,700;1,400;1,700&family=Comfortaa:wght@500&display=swap">
<style>
  :root {
    --page: #f4f5f7;
    --card: #ffffff;
    --brand-blue: #1f5fa8;
    --band-blue: #4a78bf;
    --ink: #3a3a3a;
    --muted: #555555;
    --photo-grey: #cfcfcf;
    --photo-label: #9a9a9a;
    --dusk-top: #5a6a8c;
    --dusk-mid: #9a8fa6;
    --dusk-low: #e2a77a;
  }
  * { margin: 0; padding: 0; box-sizing: border-box; }
  html, body { width: 1200px; height: 1200px; overflow: hidden; background: var(--page); }

  .signature {
    position: absolute;
    left: 100px; top: 300px;
    width: 1000px; height: 560px;
    background: var(--card);
    font-family: "Noto Serif", Georgia, serif;
    color: var(--ink);
    overflow: hidden;
  }

  .brand {
    position: absolute; right: 60px; top: 36px;
    display: flex; align-items: center; gap: 12px;
  }
  .brand__mark { width: 22px; height: 22px; background: var(--brand-blue); }
  .brand__name {
    font-family: "Noto Serif", Georgia, serif;
    font-weight: 700; font-size: 30px; letter-spacing: 1px;
    color: var(--brand-blue);
  }

  .portrait {
    position: absolute; left: 40px; top: 96px;
    width: 210px; height: 280px;
    background: var(--photo-grey);
    border-radius: 110px 16px 110px 16px;
    display: flex; align-items: center; justify-content: center;
    z-index: 2;
  }
  .portrait__label {
    transform: rotate(-60deg);
    font-family: "Comfortaa", sans-serif;
    font-size: 24px; letter-spacing: 3px;
    color: var(--photo-label);
  }

  .contact { position: absolute; left: 290px; top: 100px; }
  .contact__name {
    font-style: italic; font-weight: 700; font-size: 36px;
    color: var(--brand-blue); line-height: 1.1;
  }
  .contact__role { font-size: 19px; color: var(--muted); margin: 2px 0 16px; }
  .contact__line { font-size: 19px; line-height: 1.5; color: var(--ink); white-space: nowrap; }
  .contact__label {
    font-style: italic; color: var(--brand-blue);
    letter-spacing: 2px; margin-right: 6px;
  }
  .contact__sep { margin: 0 8px; }

  .social { display: flex; gap: 8px; margin-top: 10px; }
  .social__dot { width: 26px; height: 26px; border-radius: 50%; background: var(--brand-blue); }

  .property-view {
    position: absolute; left: 0; bottom: 0;
    width: 560px; height: 170px;
    background: linear-gradient(180deg, var(--dusk-top) 0%, var(--dusk-mid) 60%, var(--dusk-low) 100%);
  }

  .anniversary {
    position: absolute; right: 0; bottom: 70px;
    width: 690px; height: 100px;
    background: var(--band-blue);
    clip-path: polygon(50px 0, 100% 0, 100% 100%, 0 100%);
    display: flex; align-items: center; justify-content: center;
    padding: 0 20px 0 50px;
  }
  .anniversary__text {
    font-family: "Comfortaa", sans-serif; font-weight: 500;
    font-size: 28px; letter-spacing: 2px; color: #ffffff;
    text-transform: uppercase; white-space: nowrap;
  }
</style>
</head>
<body>
  <section class="signature">
    <div class="brand">
      <span class="brand__mark"></span>
      <span class="brand__name">CORVAN HOLD</span>
    </div>

    <div class="portrait"><span class="portrait__label">PHOTO</span></div>

    <div class="contact">
      <p class="contact__name">Daniel R. Ashwell</p>
      <p class="contact__role">Owner</p>
      <p class="contact__line"><span class="contact__label">Tel:</span>1300 555 019<span class="contact__sep">|</span><span class="contact__label">Fax:</span>8010 4422</p>
      <p class="contact__line"><span class="contact__label">Email:</span>admin@corvanhold.com.au<span class="contact__sep">|</span><span class="contact__label">Web:</span>www.corvanhold.com.au</p>
      <p class="contact__line">Shop 5 / 21 Bayside Lane, Marlow, NSW 2140</p>
      <div class="social"><span class="social__dot"></span><span class="social__dot"></span></div>
    </div>

    <div class="property-view" role="img" aria-label="Photo of a two-storey family home at dusk"></div>

    <div class="anniversary"><span class="anniversary__text">Celebrating 10 years in 2021</span></div>
  </section>
</body>
</html>
```